Harborline Cremations Business Cards

To create a business card for my company Harborline Cremations. Remember it is a cremation company.
We want to make sure people have a business card and information. Something modern, professional
100% Online
Prices starting at $695 all-inclusive (prices subject to change without notice).
A business card is the first point of contact with the prospective client.

Contact Information for Business Card

(305) 418-7260
www.HarborlineCremationsMiami.example
harborlinecremations@mailbox.example

Requirements
Must have
• 100% Online
Prices starting at $695 all-inclusive (prices subject to change without notice)

(305) 418-7260

Must match logo style
Should not have
• No black backgrounds. Please only use the white, orange and blue from the logo

```html
<!DOCTYPE html>
<html lang="en">
<head>
<meta charset="utf-8">
<title>Harborline Cremations – Business Cards</title>
<link href="https://fonts.googleapis.com/css2?family=Montserrat:wght@400;500;700&display=swap" rel="stylesheet">
<style>
  :root {
    --blue: #0aa0dc;
    --blue-soft: #2cb0e6;
    --orange: #f28b2c;
    --orange-light: #f6a94a;
    --white: #ffffff;
    --ink: #2b2b2b;
    --backdrop: #eef1f4;
  }
  * { box-sizing: border-box; margin: 0; padding: 0; }
  html, body {
    width: 1200px; height: 997px; overflow: hidden;
    background: var(--backdrop);
    font-family: "Montserrat", Arial, sans-serif;
  }
  .canvas { position: relative; width: 1200px; height: 997px; }

  .card {
    position: absolute; width: 620px; height: 354px;
    border-radius: 22px; overflow: hidden;
    box-shadow: 0 10px 28px rgba(0,0,0,0.16);
  }

  /* Back side */
  .card-back { left: 70px; top: 90px; background: var(--blue); }
  .card-back .pattern {
    position: absolute; inset: 0;
    background: linear-gradient(135deg, var(--blue-soft), var(--blue));
  }
  .card-back .brand {
    position: absolute; right: 36px; top: 150px;
    display: flex; align-items: center; gap: 10px;
    color: var(--white); font-weight: 700; font-size: 20px; letter-spacing: 0.5px;
  }
  .brand .dot { width: 14px; height: 14px; border-radius: 50%; background: var(--white); flex: none; }

  /* Front side */
  .card-front { left: 510px; top: 540px; background: var(--white); }
  .card-front .brand {
    position: absolute; left: 34px; top: 136px; width: 220px;
    display: flex; align-items: center; gap: 10px;
    color: var(--blue); font-weight: 700; font-size: 22px; line-height: 1.15;
  }
  .card-front .brand .dot { background: var(--orange); width: 18px; height: 18px; }
  .divider {
    position: absolute; left: 268px; top: 40px; width: 2px; height: 176px;
    background: var(--orange);
  }
  .contact { position: absolute; left: 290px; top: 40px; width: 310px; }
  .contact .person {
    color: var(--orange); font-weight: 700; font-size: 24px; letter-spacing: 0.5px;
  }
  .contact .role {
    color: var(--blue); font-weight: 500; font-size: 15px; margin-top: 2px; margin-bottom: 18px;
  }
  .contact ul { list-style: none; }
  .contact li {
    display: flex; align-items: center; gap: 8px;
    color: var(--blue); font-size: 13px; font-weight: 500; margin-bottom: 7px;
    white-space: nowrap;
  }
  .contact svg { width: 13px; height: 13px; flex: none; fill: var(--orange); }
  .online {
    position: absolute; left: 0; right: 0; top: 234px; text-align: center;
    color: var(--blue); font-size: 15px; font-weight: 500; padding-left: 120px;
  }
  .price-band {
    position: absolute; left: 0; right: 0; top: 268px; height: 38px;
    background: linear-gradient(90deg, var(--orange) 0%, var(--orange-light) 30%, #9fb4b4 60%, var(--blue) 100%);
    display: flex; align-items: center; justify-content: center; padding: 0 30px;
    color: var(--ink); font-size: 12.5px; font-weight: 500; white-space: nowrap;
  }
</style>
</head>
<body>
<main class="canvas">

  <section class="card card-back" aria-label="Business card back">
    <div class="pattern" role="img" aria-label="Repeating faint brand pattern across the blue card back"></div>
    <div class="brand"><span class="dot"></span>Harborline Cremations</div>
  </section>

  <section class="card card-front" aria-label="Business card front">
    <div class="brand"><span class="dot"></span>Harborline Cremations</div>
    <div class="divider"></div>
    <div class="contact">
      <p class="person">DANA WHITLOCK</p>
      <p class="role">Account Executive</p>
      <ul>
        <li>
          <svg viewBox="0 0 24 24"><path d="M6.6 10.8a15.1 15.1 0 0 0 6.6 6.6l2.2-2.2c.3-.3.7-.4 1-.2 1.1.4 2.3.6 3.6.6.6 0 1 .4 1 1V20c0 .6-.4 1-1 1A17 17 0 0 1 3 4c0-.6.4-1 1-1h3.5c.6 0 1 .4 1 1 0 1.3.2 2.5.6 3.6.1.3 0 .7-.2 1z"/></svg>
          (305) 418-7260
        </li>
        <li>
          <svg viewBox="0 0 24 24"><path d="M2 5h20v14H2z M2 5l10 8 10-8" /></svg>
          harborlinecremations@mailbox.example
        </li>
        <li>
          <svg viewBox="0 0 24 24"><circle cx="12" cy="12" r="10"/></svg>
          www.HarborlineCremationsMiami.example
        </li>
      </ul>
    </div>
    <p class="online">100% Online</p>
    <div class="price-band">Prices starting at $695 all-inclusive (prices subject to change without notice)</div>
  </section>

</main>
</body>
</html>
```